Brightmoor Cleaning Services

need a brochure for my cleaning company. Contact info coming soon .

Target Market(s)

Cleaning Services

Industry/Entity Type

Cleaning Service

Requirements
Must have
• I attached logo for you to use.

Corporate address -
472 Kestrel Ridge W Ste 518
Tukwila, WA 98102

Phone number - 877-514-SHINE
Nice to have
• bifold brochure. I attached some samples
Should not have
• Pictures of people. Keep it clean and professional.

```html
<!DOCTYPE html>
<html lang="en">
<head>
<meta charset="utf-8">
<title>Brightmoor Cleaning Services – Trifold Brochure</title>
<link rel="stylesheet" href="https://fonts.googleapis.com/css2?family=Oswald:wght@500;600;700&family=Montserrat:wght@400;500;600;700&display=swap">
<style>
  :root{
    --blue:#1769c9;
    --blue-deep:#0f55ad;
    --red:#e2262c;
    --ink:#2a2a2a;
    --muted:#4a4a4a;
    --paper:#ffffff;
    --backdrop:#b8b8b8;
    --green:#6cb33f;
    --amber:#f2b417;
    --head:'Oswald', 'Arial Narrow', sans-serif;
    --body:'Montserrat', Arial, sans-serif;
  }
  *{box-sizing:border-box;margin:0;padding:0}
  html,body{width:1200px;height:2326px;overflow:hidden;background:var(--backdrop)}
  .canvas{position:relative;width:1200px;height:2326px;background:var(--backdrop);font-family:var(--body);color:var(--ink)}
  .spread{position:absolute;left:60px;width:1080px;height:836px;display:flex;background:var(--paper);box-shadow:0 14px 30px rgba(0,0,0,.35);overflow:hidden}
  .spread--outside{top:200px}
  .spread--inside{top:1290px}
  .panel{position:relative;width:360px;height:836px;flex:none}
  .panel--white{background:var(--paper)}
  .panel--blue{background:linear-gradient(160deg,#1c74d6 0%,var(--blue) 50%,var(--blue-deep) 100%);color:#fff}

  .heading{font-family:var(--head);font-weight:600;font-size:22px;letter-spacing:.2px;color:var(--blue);text-transform:uppercase;line-height:1.1}
  .heading .accent{color:var(--red)}
  .heading--light{color:#fff;font-size:24px}
  .copy{font-size:9.6px;line-height:1.42;color:var(--muted);text-align:justify}
  .copy--light{color:#eaf2ff}

  /* outside, left panel */
  .reliable{padding:40px 40px 0}
  .reliable .lead{font-size:10.4px;font-weight:700;line-height:1.35;margin-top:12px;color:var(--ink)}
  .dots{color:var(--red);font-size:14px;letter-spacing:1px;line-height:1;margin-top:2px}
  .feature{margin-top:26px}
  .feature h3{display:flex;align-items:center;gap:8px;font-family:var(--head);font-weight:500;font-size:13px;color:#333;text-transform:uppercase}
  .feature h3 svg{width:18px;height:18px;flex:none}
  .feature .copy{margin-top:8px;font-size:10px}

  .photo{position:absolute;left:0;width:100%;display:block}

  /* testimonials */
  .testimonials{padding:44px 32px 0;text-align:center}
  .quote{position:relative;margin-top:26px;border:1.5px solid #fff;border-radius:12px;padding:20px 16px 14px;text-align:left}
  .quote::before,.quote::after{position:absolute;font-family:Georgia,serif;font-size:30px;line-height:1;color:#fff;background:var(--blue)}
  .quote::before{content:"\201C";top:-12px;left:12px;padding:0 4px}
  .quote::after{content:"\201D";bottom:-20px;right:10px;padding:0 4px}
  .quote p{font-size:8.4px;line-height:1.4;color:#eaf2ff}
  .quote cite{display:block;text-align:right;font-style:normal;font-weight:700;font-size:9.5px;margin-top:4px}
  .brandmark{font-family:var(--head);font-weight:600;text-transform:uppercase;line-height:1.1;text-align:center}
  .testimonials .brandmark{margin-top:58px;font-size:19px;color:#fff}

  .contact{position:relative;margin:46px 24px 0;border:1.5px solid #fff;border-radius:12px;padding:40px 10px 26px;text-align:center}
  .contact h2{position:absolute;top:-16px;left:50%;transform:translateX(-50%);padding:0 12px;background:var(--blue);font-family:var(--head);font-weight:600;font-size:20px;text-transform:uppercase}
  .contact li{list-style:none;margin-bottom:24px;font-weight:600;font-size:11px}
  .contact li:last-child{margin-bottom:0}
  .contact li.big{font-size:14px}
  .contact .dot{display:block;width:18px;height:18px;margin:0 auto 8px;border-radius:50%;background:var(--paper);position:relative}
  .contact .dot svg{position:absolute;inset:3px;width:12px;height:12px}

  /* cover */
  .cover .brandmark{position:absolute;top:34px;left:0;width:100%;font-size:21px;color:var(--blue)}
  .cover .title{position:absolute;top:536px;left:0;width:100%;text-align:center;font-family:var(--head);font-weight:700;font-size:64px;line-height:.92;text-transform:uppercase;color:var(--blue);letter-spacing:.5px}
  .cover .title span{display:block;color:var(--red)}
  .cover .tagline{position:absolute;top:680px;left:0;width:100%;text-align:center;font-size:8.4px;font-weight:700;color:#222}
  .rule{display:block;width:36px;height:3px;background:var(--blue);margin:0 auto}
  .cover .rule{position:absolute;top:703px;left:162px}
  .cover .intro{position:absolute;top:722px;left:40px;right:40px;text-align:center;font-size:10px;line-height:1.4;color:var(--muted)}
  .url-pill{position:absolute;top:770px;left:42px;right:42px;height:30px;border:1.5px solid var(--blue);border-radius:16px;display:flex;align-items:center;gap:10px;padding:0 6px;font-size:13px;color:var(--blue-deep);font-weight:500}
  .url-pill .globe{width:18px;height:18px;border-radius:50%;background:var(--blue);flex:none;position:relative}
  .url-pill .globe svg{position:absolute;inset:3px;width:12px;height:12px}

  /* inside */
  .about{padding:38px 40px 0}
  .about .copy{margin-top:8px;font-size:9.4px}
  .about .heading + .copy + .heading{margin-top:16px}
  .about-mark{position:absolute;left:40px;bottom:24px;font-size:13px;color:var(--blue);z-index:2}

  .services{padding:40px 32px 0 34px}
  .service{display:flex;gap:14px}
  .service svg{width:44px;height:44px;flex:none}
  .service h3{font-family:var(--head);font-weight:500;font-size:12.5px;line-height:1.2;text-transform:uppercase}
  .service .copy{margin-top:6px;font-size:8.6px;line-height:1.38}
  .services--light .service{margin-top:22px}
  .services--light h3{color:#fff}
  .services--dark{padding:380px 28px 0 36px}
  .services--dark .service{margin-top:30px}
  .services--dark .service:first-child{margin-top:0}
  .services--dark h3{color:var(--blue)}
  .services--dark svg{width:36px;height:36px}
</style>
</head>
<body>
<main class="canvas">

  <!-- Outside spread -->
  <section class="spread spread--outside" aria-label="Brochure outside">
    <article class="panel panel--white">
      <div class="reliable">
        <h2 class="heading">Reliable <span class="accent">Cleaning</span></h2>
        <p class="lead">Lorem Ipsum is simply dummy text of the printing and typesetting industry. Lorem Ipsum has been the industry's standard dummy text ever</p>
        <div class="dots">••••</div>

        <div class="feature">
          <h3><svg viewBox="0 0 20 20"><path d="M3 17C4 8 10 4 18 3c-1 8-6 13-14 13z" fill="var(--green)"/></svg>Green Products</h3>
          <p class="copy">Lorem Ipsum is simply dummy text of the printing and typesetting industry. Lorem Ipsum has been the industry's standard dummy text ever</p>
        </div>
        <div class="feature">
          <h3><svg viewBox="0 0 20 20"><rect x="3" y="4" width="14" height="13" rx="1" fill="#f2c9d0"/><rect x="3" y="4" width="14" height="4" fill="var(--red)"/><rect x="6" y="10" width="2" height="2" fill="#b05"/><rect x="10" y="10" width="2" height="2" fill="#b05"/><rect x="6" y="13" width="2" height="2" fill="#b05"/></svg>Flexible Scheduling</h3>
          <p class="copy">Lorem Ipsum is simply dummy text of the printing and typesetting industry. Lorem Ipsum has been the industry's standard dummy text ever</p>
        </div>
        <div class="feature">
          <h3><svg viewBox="0 0 20 20"><rect x="5" y="3" width="10" height="15" fill="var(--amber)"/><rect x="7" y="6" width="2" height="2" fill="#fff"/><rect x="11" y="6" width="2" height="2" fill="#fff"/><rect x="7" y="10" width="2" height="2" fill="#fff"/><rect x="11" y="10" width="2" height="2" fill="#fff"/></svg>Residential</h3>
          <p class="copy">Lorem Ipsum is simply dummy text of the printing and typesetting industry. Lorem Ipsum has been the industry's standard dummy text ever</p>
        </div>
        <div class="feature">
          <h3><svg viewBox="0 0 20 20"><circle cx="6" cy="6" r="3" fill="var(--red)"/><circle cx="14" cy="6" r="3" fill="var(--amber)"/><path d="M2 17a5 5 0 0 1 8-4v4z" fill="var(--blue)"/><path d="M10 17v-4a5 5 0 0 1 8 4z" fill="var(--blue-deep)"/></svg>Commercial</h3>
          <p class="copy">Lorem Ipsum is simply dummy text of the printing and typesetting industry. Lorem Ipsum has been the industry's standard dummy text ever</p>
        </div>
      </div>
      <svg class="photo" style="top:500px;height:336px" viewBox="0 500 360 336" role="img" aria-label="Photo: smiling cleaner in an apron holding a scrub brush and spray bottle">
        <defs><linearGradient id="g-cleaner" x1="0" y1="0" x2="1" y2="1"><stop offset="0" stop-color="#eef2f6"/><stop offset=".6" stop-color="#d9dfe6"/><stop offset="1" stop-color="#bcc8d4"/></linearGradient></defs>
        <path d="M0 560C110 505 250 530 360 640V836H0Z" fill="url(#g-cleaner)"/>
        <path d="M0 560C110 505 250 530 360 640" fill="none" stroke="var(--blue)" stroke-width="11"/>
      </svg>
    </article>

    <article class="panel panel--blue">
      <div class="testimonials">
        <h2 class="heading heading--light">Testimonials</h2>
        <blockquote class="quote">
          <p>Lorem Ipsum is simply dummy text of the printing and typesetting industry. Lorem Ipsum has been the industry's standard dummy text ever since the 1500s, when an unknown printer took a galley of type and scrambled it</p>
          <cite>-Dana Whitfield</cite>
        </blockquote>
        <blockquote class="quote">
          <p>Lorem Ipsum is simply dummy text of the printing and typesetting industry. Lorem Ipsum has been the industry's standard dummy text ever since the 1500s, when an unknown printer took a galley of type and scrambled it</p>
          <cite>-Marcus Lee</cite>
        </blockquote>
        <p class="brandmark">Brightmoor<br>Cleaning Services</p>
      </div>
      <div class="contact">
        <h2>Contact</h2>
        <ul>
          <li class="big"><span class="dot"><svg viewBox="0 0 12 12"><path d="M3 1l2 2-1 1.5a6 6 0 0 0 3.5 3.5L9 7l2 2-1.5 2C5 11 1 7 1 2.5z" fill="var(--red)"/></svg></span>877-514-SHINE</li>
          <li><span class="dot"><svg viewBox="0 0 12 12"><path d="M6 11S2 7 2 4.5a4 4 0 0 1 8 0C10 7 6 11 6 11z" fill="var(--red)"/><circle cx="6" cy="4.5" r="1.4" fill="#fff"/></svg></span>472 Kestrel Ridge W Ste 518<br>Tukwila, WA 98102</li>
          <li><span class="dot"><svg viewBox="0 0 12 12"><rect x="1.5" y="3" width="9" height="6" rx="1" fill="var(--red)"/><path d="M1.5 3.5L6 7l4.5-3.5" fill="none" stroke="#fff" stroke-width=".9"/></svg></span>info@brightmoorclean.com</li>
          <li><span class="dot"><svg viewBox="0 0 12 12"><circle cx="6" cy="6" r="5" fill="var(--red)"/><path d="M1 6h10M6 1c-2 3-2 7 0 10M6 1c2 3 2 7 0 10" fill="none" stroke="#fff" stroke-width=".8"/></svg></span>www.brightmoorclean.com</li>
        </ul>
      </div>
    </article>

    <article class="panel panel--white cover">
      <p class="brandmark">Brightmoor<br>Cleaning Services</p>
      <svg class="photo" style="top:92px;height:400px" viewBox="0 92 360 400" role="img" aria-label="Photo: two cleaners in blue overalls cleaning an office desk">
        <defs><linearGradient id="g-team" x1="0" y1="0" x2="1" y2="1"><stop offset="0" stop-color="#f1f3f6"/><stop offset=".5" stop-color="#c9d6e6"/><stop offset="1" stop-color="#7fa3cf"/></linearGradient></defs>
        <path d="M0 92H360V420C290 470 190 480 110 450 60 432 25 410 0 396Z" fill="url(#g-team)"/>
        <path d="M0 396C25 410 60 432 110 450 190 480 290 470 360 420" fill="none" stroke="var(--blue)" stroke-width="12"/>
      </svg>
      <h1 class="title">Cleaning<span>Services</span></h1>
      <p class="tagline">LOREM IPSUM DOLOR SAIL GATO MI PIACC EREBE UNA.</p>
      <span class="rule"></span>
      <p class="intro">Lorem Ipsum is simply dummy text of the printing and typesetting industry.</p>
      <p class="url-pill"><span class="globe"><svg viewBox="0 0 12 12"><circle cx="6" cy="6" r="5" fill="none" stroke="#fff" stroke-width=".9"/><path d="M1 6h10M6 1c-2 3-2 7 0 10M6 1c2 3 2 7 0 10" fill="none" stroke="#fff" stroke-width=".8"/></svg></span>www.brightmoorclean.com</p>
    </article>
  </section>

  <!-- Inside spread -->
  <section class="spread spread--inside" aria-label="Brochure inside">
    <article class="panel panel--white">
      <div class="about">
        <h2 class="heading">Why <span class="accent">Choose Us</span></h2>
        <p class="copy">Lorem Ipsum is simply dummy text of the printing and typesetting industry. Lorem Ipsum has been the industry's standard dummy text ever since the 1500s, when an unknown printer took a galley of type and scrambled it to make a type specimen book. It has survived not only five centuries, but also the leap into electronic typesetting, remaining essentially unchanged. It was popularised in the 1960s with the release of Letraset sheets containing Lorem Ipsum passages, and more recently with desktop publishing software like Aldus PageMaker including versions of Lorem Ipsum.</p>
        <h2 class="heading">About <span class="accent">Us</span></h2>
        <p class="copy">Lorem Ipsum is simply dummy text of the printing and typesetting industry. Lorem Ipsum has been the industry's standard dummy text ever since the 1500s, when an unknown printer took a galley of type and scrambled it to make a type specimen book. It has survived not only five centuries, but also the leap into electronic typesetting, remaining essentially unchanged. It was popularised in the 1960s with the release of Letraset sheets containing Lorem Ipsum passages, and more recently with desktop publishing software like Aldus PageMaker including versions of Lorem Ipsum. Lorem Ipsum is simply dummy text of the printing and typesetting industry, remaining essentially unchanged.</p>
      </div>
      <p class="brandmark about-mark">Brightmoor</p>
    </article>

    <article class="panel panel--blue">
      <div class="services services--light">
        <h2 class="heading heading--light" style="font-size:20px">Our Services</h2>
        <div class="service">
          <svg viewBox="0 0 44 44" fill="none" stroke="#fff" stroke-width="1.6"><path d="M14 4v24M8 28h12l2 10H6z"/><path d="M26 26h12l-2 12H28z"/><circle cx="34" cy="18" r="2"/><circle cx="30" cy="14" r="1.4"/></svg>
          <div><h3>Floor Cleaning</h3><p class="copy copy--light">Lorem Ipsum is simply dummy text of the printing and typesetting industry. Lorem Ipsum has been the industry's standard dummy text ever since the 1500s, when an unknown printer took a galley of type and scrambled it to make a type specimen book. It has survived not only five centuries, but also the leap into electronic typesetting.</p></div>
        </div>
        <div class="service">
          <svg viewBox="0 0 44 44" fill="none" stroke="#fff" stroke-width="1.6"><rect x="6" y="6" width="30" height="30"/><path d="M6 21h30M21 6v30M12 30l16-16"/></svg>
          <div><h3>Window Cleaning</h3><p class="copy copy--light">Lorem Ipsum is simply dummy text of the printing and typesetting industry. Lorem Ipsum has been the industry's standard dummy text ever since the 1500s, when an unknown printer took a galley of type and scrambled it to make a type specimen book. It has survived not only five centuries, but also the leap into electronic typesetting.</p></div>
        </div>
        <div class="service">
          <svg viewBox="0 0 44 44" fill="none" stroke="#fff" stroke-width="1.6"><path d="M4 30L12 12h20l8 18z"/><path d="M8 21h28M14 12l-4 18M22 12v18M30 12l4 18"/></svg>
          <div><h3>Roof Cleaning</h3><p class="copy copy--light">Lorem Ipsum is simply dummy text of the printing and typesetting industry. Lorem Ipsum has been the industry's standard dummy text ever since the 1500s, when an unknown printer took a galley of type and scrambled it to make a type specimen book. It has survived not only five centuries, but also the leap into electronic typesetting.</p></div>
        </div>
      </div>
    </article>

    <article class="panel panel--white">
      <svg class="photo" style="top:0;height:360px" viewBox="0 0 360 360" role="img" aria-label="Photo: mop and bucket with gloves on a glossy floor by a window">
        <defs><linearGradient id="g-mop" x1="0" y1="0" x2="1" y2="1"><stop offset="0" stop-color="#f4f6f8"/><stop offset=".55" stop-color="#d7e3ee"/><stop offset="1" stop-color="#6fb5e0"/></linearGradient></defs>
        <path d="M0 0H360V318C290 330 200 312 130 280 80 257 40 230 0 218Z" fill="url(#g-mop)"/>
        <path d="M0 218C40 230 80 257 130 280 200 312 290 330 360 318" fill="none" stroke="var(--blue)" stroke-width="12"/>
      </svg>
      <div class="services services--dark">
        <div class="service">
          <svg viewBox="0 0 36 36" fill="none" stroke="var(--red)" stroke-width="1.6"><path d="M8 10h20M14 10V6h8v4M10 10l2 22h12l2-22M15 15v12M18 15v12M21 15v12"/></svg>
          <div><h3>Trash Cleaning</h3><p class="copy">Lorem Ipsum is simply dummy text of the printing and typesetting industry. Lorem Ipsum has been the industry's standard dummy text ever since the 1500s, when an unknown printer took a galley of type and scrambled it to make a type specimen book. It has survived not only five centuries, but also the leap into electronic typesetting, remaining essentially unchanged.</p></div>
        </div>
        <div class="service">
          <svg viewBox="0 0 36 36" fill="none" stroke="var(--red)" stroke-width="1.6"><path d="M8 14v-3h20v3M4 14h6v6h16v-6h6v10H4zM7 24v4M29 24v4"/></svg>
          <div><h3>Sofa Cleaning</h3><p class="copy">Lorem Ipsum is simply dummy text of the printing and typesetting industry. Lorem Ipsum has been the industry's standard dummy text ever since the 1500s, when an unknown printer took a galley of type and scrambled it to make a type specimen book. It has survived not only five centuries, but also the leap into electronic typesetting, remaining essentially unchanged.</p></div>
        </div>
        <div class="service">
          <svg viewBox="0 0 36 36" fill="none" stroke="var(--red)" stroke-width="1.6"><path d="M4 14L18 5l14 9v18H4z"/><rect x="9" y="17" width="18" height="15"/><path d="M9 21h18M9 25h18"/></svg>
          <div><h3>Garage Cleaning</h3><p class="copy">Lorem Ipsum is simply dummy text of the printing and typesetting industry. Lorem Ipsum has been the industry's standard dummy text ever since the 1500s, when an unknown printer took a galley of type and scrambled it to make a type specimen book. It has survived not only five centuries, but also the leap into electronic typesetting, remaining essentially unchanged.</p></div>
        </div>
      </div>
    </article>

    <svg class="photo" style="top:500px;left:0;width:720px;height:336px" viewBox="0 500 720 336" role="img" aria-label="Photo: cleaner in a teal uniform wiping a kitchen counter">
      <defs><linearGradient id="g-kitchen" x1="0" y1="0" x2="1" y2="1"><stop offset="0" stop-color="#eef1f3"/><stop offset=".5" stop-color="#d3d9dd"/><stop offset="1" stop-color="#2f8c9a"/></linearGradient></defs>
      <path d="M0 560C180 480 430 500 720 720V836H0Z" fill="url(#g-kitchen)"/>
      <path d="M0 560C180 480 430 500 720 720" fill="none" stroke="var(--blue)" stroke-width="12"/>
    </svg>
  </section>

</main>
</body>
</html>
```